Ridgeway Auto Care
Ridgeway Auto Care - Automotive
Creative Brief
Professional
Dale Morrow
President
4817 Silver Fern Ln Braselton,GA 30519
d.morrow@ridgewayautocare.example
www.ridgewayautocare.example

```html
<!DOCTYPE html>
<html lang="en">
<head>
<meta charset="utf-8">
<title>Ridgeway Auto Care – Stationery Set</title>
<link href="https://fonts.googleapis.com/css2?family=Roboto+Condensed:wght@400;700&display=swap" rel="stylesheet">
<style>
  :root{
    --red:#d4161b;
    --red-deep:#7a0508;
    --red-dark:#4a0204;
    --paper:#ffffff;
    --ink:#222;
    --muted:#555;
    --stage:#8e8e8e;
    --stage-light:#a9a9a9;
    --black:#151515;
    --silver:#c9c9c9;
    --rule:#cfcfcf;
  }
  *{box-sizing:border-box;margin:0;padding:0}
  html,body{width:1200px;height:269px;overflow:hidden}
  body{font-family:"Roboto Condensed",Arial,sans-serif;background:var(--red)}
  .sheet{position:relative;width:1200px;height:269px;border:7px solid var(--red);
    background:radial-gradient(ellipse at 50% 50%,var(--stage-light),var(--stage))}
  .piece{position:absolute;box-shadow:0 2px 4px rgba(0,0,0,.35);overflow:hidden}
  .red-face{background:radial-gradient(ellipse at 55% 40%,var(--red) 0%,var(--red-deep) 70%,var(--red-dark) 100%)}
  .brand{display:flex;flex-direction:column;align-items:center;gap:2px;color:var(--ink);font-weight:700;text-align:center;line-height:1;white-space:nowrap}
  .brand .mark{border-radius:50%;background:currentColor;flex:none}
  .on-red{color:#fff}

  /* business cards */
  .card{width:72px;height:40px;background:var(--paper)}
  .card::before{content:"";position:absolute;left:0;bottom:0;width:34px;height:10px;background:var(--red);clip-path:polygon(0 0,100% 100%,0 100%)}
  .card .brand{position:absolute;top:7px;left:0;right:0;font-size:4px}
  .card .brand .mark{width:10px;height:10px}
  .card-back{width:72px;height:40px;background:var(--black)}
  .card-back .mark{position:absolute;left:23px;top:7px;width:26px;height:26px;border-radius:50%;background:radial-gradient(circle,#eee,var(--silver) 60%,#777)}

  /* letterhead */
  .letterhead{left:115px;top:32px;width:74px;height:206px;background:var(--paper)}
  .letterhead .corner{position:absolute;left:0;top:0;width:24px;height:14px;background:var(--red);clip-path:polygon(0 0,100% 0,0 100%)}
  .letterhead .foot{position:absolute;left:0;right:0;bottom:0;height:10px;background:var(--red);clip-path:polygon(0 40%,100% 0,100% 100%,0 100%)}
  .letterhead .brand{position:absolute;top:8px;left:0;right:0;font-size:4px}
  .letterhead .brand .mark{width:11px;height:11px}
  .letterhead .contact{position:absolute;bottom:13px;left:3px;right:3px;text-align:center;font-size:2.4px;color:var(--muted);line-height:1.4;white-space:nowrap}

  /* envelopes */
  .envelope{left:214px;width:146px;height:34px;background:var(--paper)}
  .envelope .flap{position:absolute;left:0;top:0;width:100%;height:16px;background:#eee;clip-path:polygon(0 0,100% 0,50% 100%)}
  .envelope .band{position:absolute;left:0;bottom:0;width:34px;height:8px;background:var(--red);clip-path:polygon(0 0,100% 100%,0 100%)}
  .envelope .brand{position:absolute;left:6px;top:5px;font-size:3.5px;flex-direction:row}
  .envelope .brand .mark{width:6px;height:6px}

  /* small red cards */
  .tag{left:504px;top:77px;width:44px;height:42px}
  .tag .brand{margin-top:8px;font-size:3.5px}
  .tag .brand .mark{width:12px;height:12px}
  .slip{left:499px;top:173px;width:66px;height:33px}
  .slip .brand{margin-top:7px;font-size:3.5px}
  .slip .brand .mark{width:9px;height:9px}

  /* folder */
  .folder{left:607px;top:19px;width:194px;height:222px}
  .folder .panel{position:absolute;top:0;height:100%;width:50%}
  .folder .panel.left{left:0;background:radial-gradient(ellipse at 60% 35%,#b10f13,var(--red-dark) 80%)}
  .folder .panel.right{right:0;background:radial-gradient(ellipse at 50% 35%,var(--red) 0%,var(--red-deep) 75%)}
  .folder .brand{position:absolute;top:18px;left:0;right:0;font-size:4.5px}
  .folder .brand .mark{width:16px;height:16px}
  .folder .pocket{position:absolute;bottom:0;height:66px;width:50%;background:linear-gradient(#2a2a2a,var(--black))}
  .folder .pocket.left{left:0;clip-path:polygon(0 30%,100% 0,100% 100%,0 100%)}
  .folder .pocket.right{right:0;clip-path:polygon(0 0,100% 30%,100% 100%,0 100%)}
  .folder .slot-card{position:absolute;right:26px;bottom:20px;width:40px;height:22px;background:var(--red-deep);border:1px solid #000}

  /* cd */
  .cd-sleeve{left:832px;top:100px;width:48px;height:48px}
  .cd-disc{left:850px;top:86px;width:58px;height:58px;border-radius:50%;background:radial-gradient(circle,#fff 0 5px,#ddd 5px 7px,var(--red) 8px,var(--red-deep) 100%)}
  .cd-disc .brand{position:absolute;top:7px;left:0;right:0;font-size:3.5px}

  /* fax */
  .fax{left:998px;top:34px;width:150px;height:206px;background:var(--paper)}
  .fax .brand{position:absolute;top:8px;left:8px;font-size:4px;flex-direction:row}
  .fax .brand .mark{width:7px;height:7px}
  .fax h1{position:absolute;top:20px;left:8px;font-size:12px;font-weight:400;color:var(--ink)}
  .fax .fields{position:absolute;top:40px;left:8px;right:8px;list-style:none;font-size:3.5px;color:var(--muted)}
  .fax .fields li{border-bottom:1px solid var(--rule);padding:3px 0 1px}
  .fax .foot{position:absolute;left:0;right:0;bottom:0;height:10px;background:var(--red);clip-path:polygon(0 40%,100% 0,100% 100%,0 100%)}
</style>
</head>
<body>
<main class="sheet">

  <div class="piece card" style="left:30px;top:78px">
    <div class="brand"><span class="mark"></span>Ridgeway Auto Care</div>
  </div>
  <div class="piece card" style="left:30px;top:124px">
    <div class="brand"><span class="mark"></span>Ridgeway Auto Care</div>
  </div>
  <div class="piece card-back" style="left:30px;top:170px"><span class="mark"></span></div>

  <section class="piece letterhead">
    <span class="corner"></span>
    <div class="brand"><span class="mark"></span>Ridgeway Auto Care</div>
    <p class="contact">Dale Morrow, President<br>4817 Silver Fern Ln Ridgeway Springs,XX 00000<br>d.morrow@ridgewayautocare.example<br>www.ridgewayautocare.example</p>
    <span class="foot"></span>
  </section>

  <div class="piece envelope" style="top:96px">
    <span class="flap"></span><span class="band"></span>
  </div>
  <div class="piece envelope" style="top:142px">
    <div class="brand"><span class="mark"></span>Ridgeway Auto Care</div>
    <span class="band"></span>
  </div>

  <div class="piece red-face tag"><div class="brand on-red"><span class="mark"></span>Ridgeway Auto Care</div></div>
  <div class="piece red-face slip"><div class="brand on-red"><span class="mark"></span>Ridgeway Auto Care</div></div>

  <section class="piece folder">
    <div class="panel left"></div>
    <div class="panel right"><div class="brand on-red"><span class="mark"></span>Ridgeway Auto Care</div></div>
    <div class="pocket left"></div>
    <div class="pocket right"></div>
    <div class="slot-card"></div>
  </section>

  <div class="piece red-face cd-sleeve"></div>
  <div class="piece cd-disc"><div class="brand on-red">Ridgeway</div></div>

  <section class="piece fax">
    <div class="brand"><span class="mark"></span>Ridgeway Auto Care</div>
    <h1>Fax</h1>
    <ul class="fields"><li>To:</li><li>From:</li><li>Date:</li><li>Pages:</li><li>Subject:</li></ul>
    <span class="foot"></span>
  </section>

</main>
</body>
</html>
```